Post Lockdown Ortho Special

We are running a special for (Ortho) Braces/Clear Aligner (Quorventa), till July 31st 2020. Up to $2,000 off with free Consultation and Xrays.

We need a ad to run in different formats.

Maybe something with: what better time to get braces when you have to wear a mask all the time.

Trying to rebuild our business and get people in for free consultations.

```html
<!DOCTYPE html>
<html lang="en">
<head>
<meta charset="utf-8">
<title>Post Lockdown Ortho Special</title>
<link href="https://fonts.googleapis.com/css2?family=Montserrat:ital,wght@0,500;1,800&family=Open+Sans:wght@600;700&display=swap" rel="stylesheet">
<style>
  :root {
    --cream: #fdfcd9;
    --white: #ffffff;
    --purple: #6c4398;
    --gold: #fce51a;
    --ribbon-start: #ffe600;
    --ribbon-end: #ffa800;
  }
  html, body { margin: 0; padding: 0; overflow: hidden; }
  body { width: 1200px; height: 675px; }
  .ad {
    position: relative;
    width: 1200px;
    height: 675px;
    overflow: hidden;
    background: var(--cream);
    font-family: "Open Sans", Arial, sans-serif;
  }
  .backdrop { position: absolute; inset: 0; }
  .photo-area { position: absolute; left: 330px; top: 18px; }
  .headline-panel {
    position: absolute;
    left: 78px; top: 58px;
    width: 442px; height: 186px;
    background: var(--purple);
  }
  .headline {
    position: absolute;
    left: 108px; top: 104px;
    margin: 0;
    font-family: "Montserrat", sans-serif;
    font-weight: 500;
    font-size: 25px;
    line-height: 30px;
    color: var(--white);
  }
  .ribbon {
    position: absolute;
    left: 58px; top: 38px;
    width: 196px; height: 56px;
    background: linear-gradient(135deg, var(--ribbon-start), var(--ribbon-end));
    transform: rotate(-4deg);
    box-shadow: 2px 4px 8px rgba(0,0,0,.18);
    display: flex; align-items: center; justify-content: center;
  }
  .ribbon span {
    font-family: "Montserrat", sans-serif;
    font-style: italic;
    font-weight: 800;
    font-size: 18px;
    color: var(--purple);
    letter-spacing: .3px;
    transform: translate(4px, 3px);
  }
  .service {
    position: absolute;
    left: 80px; top: 259px;
    margin: 0;
    font-weight: 600;
    font-size: 17px;
    line-height: 23px;
    color: var(--purple);
  }
  .deadline {
    position: absolute;
    left: 78px; top: 320px;
    width: 272px; height: 58px;
    background: var(--purple);
    box-sizing: border-box;
    padding: 7px 0 0 7px;
    font-weight: 700;
    font-size: 18px;
    line-height: 21px;
    color: var(--gold);
  }
  .discount {
    position: absolute;
    left: 852px; top: 498px;
    display: flex; align-items: center;
    color: var(--white);
  }
  .discount-lead {
    font-weight: 600;
    font-size: 22px;
    line-height: 24px;
    margin-right: 10px;
    margin-top: 6px;
  }
  .discount-amount {
    font-weight: 700;
    font-size: 76px;
    line-height: 80px;
    letter-spacing: -3px;
  }
  .discount-tail {
    font-weight: 600;
    font-size: 22px;
    transform: rotate(-90deg);
    margin-left: 6px;
  }
  .bonus {
    position: absolute;
    left: 856px; top: 579px;
    width: 280px; height: 37px;
    box-sizing: border-box;
    border: 2px solid var(--white);
    display: flex; align-items: center; justify-content: center;
    font-weight: 600;
    font-size: 15.5px;
    color: var(--white);
  }
  .practice {
    position: absolute;
    left: 47px; top: 548px;
    display: flex; align-items: center; gap: 14px;
  }
  .practice-mark {
    width: 58px; height: 58px;
    border-radius: 50%;
    background: var(--purple);
  }
  .practice-text {
    font-weight: 600;
    color: var(--purple);
    line-height: 1.25;
  }
  .practice-name { font-size: 19px; }
  .practice-doctor { font-size: 12px; letter-spacing: 1px; }
</style>
</head>
<body>
<main class="ad">
  <svg class="backdrop" width="1200" height="675" viewBox="0 0 1200 675">
    <polygon points="0,347 620,675 0,675" fill="var(--white)"/>
  </svg>

  <svg class="photo-area" width="540" height="657" viewBox="0 0 540 657" role="img" aria-label="Photo of an excited young woman in glasses and a mustard cardigan, pointing upward">
    <defs>
      <linearGradient id="photoTone" x1="0" y1="0" x2="0" y2="1">
        <stop offset="0" stop-color="#6b5146"/>
        <stop offset=".45" stop-color="#e2b9a2"/>
        <stop offset=".72" stop-color="#d9a340"/>
        <stop offset="1" stop-color="#c98f22"/>
      </linearGradient>
      <linearGradient id="photoFade" x1="0" y1="0" x2="1" y2="0">
        <stop offset="0" stop-color="#fff" stop-opacity="0"/>
        <stop offset=".15" stop-color="#fff" stop-opacity="1"/>
        <stop offset=".85" stop-color="#fff" stop-opacity="1"/>
        <stop offset="1" stop-color="#fff" stop-opacity="0"/>
      </linearGradient>
      <mask id="photoMask">
        <rect width="540" height="657" fill="url(#photoFade)"/>
      </mask>
    </defs>
    <rect width="540" height="657" rx="24" fill="url(#photoTone)" mask="url(#photoMask)"/>
  </svg>

  <div class="headline-panel"></div>

  <svg class="backdrop" width="1200" height="675" viewBox="0 0 1200 675">
    <polygon points="1200,253 444,675 1200,675" fill="var(--purple)"/>
  </svg>

  <div class="ribbon"><span>SPECIAL OFFER</span></div>

  <p class="headline">What better time to get<br>braces when you have to<br>wear a mask all the time.</p>

  <p class="service">(ORTHO) BRACES/CLEAR<br>ALIGNER (QUORVENTA)</p>

  <div class="deadline">OFFER GOOD TILL<br>JULY 31ST 2020</div>

  <div class="discount">
    <div class="discount-lead">UP<br>TO</div>
    <div class="discount-amount">$2,000</div>
    <div class="discount-tail">OFF</div>
  </div>

  <div class="bonus">with free Consultation and Xrays.</div>

  <div class="practice">
    <div class="practice-mark"></div>
    <div class="practice-text">
      <div class="practice-name">Pinecrest Family Dentistry</div>
      <div class="practice-doctor">Dr Helena Marsh</div>
    </div>
  </div>
</main>
</body>
</html>
```